Pinecrest Artisan League Membership

UPDATED files - 06/03/2021
Digital brochure needed for construction contractor related nonprofit organization.
Document will be primarily for digital viewing with potential for print version. Should be branded with our branding (logo attached). This is intended to be a multiple page document, plan to print and web (email) use. Standard Letter size document 8.5 x 11 inch
Portrait format preferred
The attached project brief includes a cover, 4 internal pages, and a back cover. This is flexible pending design layout
Target Market(s)
Residential construction business owners
Requirements
Must have
- See attached brief.Orange color palette: RGB: (253,153,0)
Nice to have
- See attached bief
Should not have
- No suit or ties. button up shirt okay, but not white collar worker.

```html
<!DOCTYPE html>
<html lang="en">
<head>
<meta charset="utf-8">
<title>Pinecrest Artisan League Membership Brochure</title>
<link rel="stylesheet" href="https://fonts.googleapis.com/css2?family=Montserrat:wght@600;800;900&family=Open+Sans:wght@400;600&display=swap">
<style>
:root{
  --orange:#fd9900;
  --ink:#1e1e22;
  --grey:#6b6b70;
  --paper:#ffffff;
  --backdrop:#e4e4e7;
  --photo-site:linear-gradient(135deg,#c9a45a 0%,#7f8a8c 45%,#3d4a52 100%);
  --photo-desk:linear-gradient(135deg,#a57a52 0%,#6b5141 55%,#2f2a28 100%);
  --photo-team:linear-gradient(135deg,#b98a5e 0%,#8a6a50 50%,#4a3c34 100%);
  --photo-city:linear-gradient(180deg,#1d2a44 0%,#2c3a5a 55%,#b07a32 100%);
}
*{box-sizing:border-box;margin:0;padding:0}
html,body{width:669px;height:1200px;overflow:hidden}
body{background:var(--backdrop);font-family:"Open Sans",Arial,sans-serif;color:var(--ink);position:relative}
.page{background:var(--paper);position:absolute;box-shadow:0 2px 6px rgba(0,0,0,.08);overflow:hidden}
.photo{position:absolute}
.site{background:var(--photo-site)}
.desk{background:var(--photo-desk)}
.team{background:var(--photo-team)}
.city{background:var(--photo-city)}
.brand{font-family:"Montserrat",Arial,sans-serif;font-weight:900;color:var(--ink);text-transform:uppercase;line-height:1.05;letter-spacing:.3px}
.rule{position:absolute;height:3px;background:var(--orange)}
.title{position:absolute;font-family:"Montserrat",Arial,sans-serif;font-weight:900;text-transform:uppercase;line-height:1;color:var(--ink);white-space:nowrap}
.title span{color:var(--orange)}
.subtitle{position:absolute;font-family:"Montserrat",Arial,sans-serif;font-weight:600;text-transform:uppercase;color:var(--grey);letter-spacing:1px;white-space:nowrap}
.head{font-family:"Montserrat",Arial,sans-serif;font-weight:800;text-transform:uppercase;font-size:7px;color:var(--ink);margin-bottom:4px}
.body{font-size:5.2px;line-height:1.55;color:var(--grey);margin-bottom:5px}
.block{position:absolute}
.marker{display:block;width:24px;height:3px;background:var(--orange);margin-bottom:5px}
.benefits{list-style:none;font-size:5.2px;line-height:1.8;color:var(--grey);columns:2;column-gap:10px}
.benefits li::before{content:"";display:inline-block;width:4px;height:4px;background:var(--orange);margin-right:4px;vertical-align:middle}
.contact-row{display:flex;align-items:center;gap:6px;margin-bottom:6px;font-size:5.2px;color:var(--grey)}
.contact-row .dot{width:12px;height:12px;border-radius:50%;background:var(--orange);flex:none}
.fold{position:absolute;top:0;bottom:0;left:50%;width:1px;background:rgba(0,0,0,.06)}
.contact{font-size:5px;line-height:1.6;color:var(--grey)}
</style>
</head>
<body>

<!-- Front cover -->
<section class="page cover" style="left:214px;top:30px;width:240px;height:310px">
  <div class="block brand" style="left:18px;top:14px;width:120px;font-size:10px">Pinecrest Artisan League</div>
  <div class="photo site" style="left:0;top:44px;width:240px;height:148px" role="img" aria-label="Construction workers in hard hats and safety vests reviewing plans on a laptop"></div>
  <div class="rule" style="left:0;top:192px;width:240px"></div>
  <div class="title" style="left:22px;top:226px;font-size:20px">Title <span>Goes Here</span></div>
  <div class="subtitle" style="left:22px;top:252px;font-size:8px">Subtitle goes here</div>
  <div class="rule" style="left:22px;top:268px;width:60px"></div>
  <div class="rule" style="left:0;bottom:0;width:240px;height:8px"></div>
</section>

<!-- Inner spread -->
<section class="page spread" style="left:45px;top:378px;width:580px;height:375px">
  <div class="fold"></div>

  <!-- left page -->
  <div class="block" style="left:20px;top:20px;width:110px">
    <p class="head">About the League</p>
    <p class="body">We unite residential builders who value honest work, safe sites and lasting craft in every home we help build.</p>
    <p class="body">Our members share tools, training and trusted referrals across every trade, from framing to finish work.</p>
    <p class="body">Founded by local builders, we keep standards high and paperwork simple.</p>
  </div>
  <div class="photo desk" style="left:140px;top:20px;width:132px;height:130px" role="img" aria-label="Contractor working at a desk with laptop and coffee"></div>
  <div class="photo team" style="left:0;top:164px;width:135px;height:112px" role="img" aria-label="Team meeting around a table reviewing project documents"></div>
  <div class="block" style="left:147px;top:168px;width:125px">
    <span class="marker"></span>
    <p class="head">Our Mission</p>
    <p class="body">Stronger contractors build stronger neighborhoods, one project at a time. We speak up for small firms and keep them informed.</p>
  </div>
  <div class="block" style="left:20px;top:292px;width:110px">
    <span class="marker"></span>
    <p class="head">Training</p>
    <p class="body">Hands-on safety and code sessions held each season for crews and owners.</p>
  </div>
  <div class="block" style="left:147px;top:292px;width:125px">
    <span class="marker"></span>
    <p class="head">Networking</p>
    <p class="body">Monthly meetups connect builders, suppliers and inspectors in one room.</p>
  </div>

  <!-- right page -->
  <div class="block" style="left:310px;top:20px;width:250px">
    <p class="head">Membership Benefits</p>
    <p class="body">Join a community that stands behind your business from first bid to final handover. Members gain access to shared resources, group rates and expert advice.</p>
    <ul class="benefits">
      <li>Safety training sessions</li>
      <li>Peer referral network</li>
      <li>Code update briefings</li>
      <li>Member events</li>
      <li>Group insurance rates</li>
      <li>Supplier discounts</li>
    </ul>
  </div>
  <div class="block" style="left:310px;top:130px;width:250px">
    <div class="contact-row"><span class="dot"></span><span>Call our member desk any weekday.</span></div>
    <div class="contact-row"><span class="dot"></span><span>Visit an open house near you.</span></div>
  </div>
  <div class="photo city" style="left:310px;top:200px;width:250px;height:150px" role="img" aria-label="City skyline at dusk with lit buildings"></div>
</section>

<!-- Outer spread: back and front cover -->
<section class="page spread" style="left:45px;top:790px;width:580px;height:375px">
  <div class="fold"></div>
  <!-- back cover -->
  <div class="block" style="left:28px;top:150px;width:150px">
    <div class="brand" style="font-size:11px">Pinecrest Artisan League</div>
    <div class="rule" style="position:static;width:50px;margin:6px 0"></div>
    <p class="contact">1200 Ridge Road, Pinecrest</p>
    <p class="contact">hello@pinecrestleague.org</p>
    <p class="contact">(555) 014-2290</p>
  </div>
  <!-- front cover -->
  <div class="block brand" style="left:420px;top:24px;width:140px;font-size:11px;text-align:right">Pinecrest Artisan League</div>
  <div class="photo site" style="left:330px;top:60px;width:230px;height:150px" role="img" aria-label="Construction workers in hard hats and safety vests reviewing plans on a laptop"></div>
  <div class="rule" style="left:330px;top:210px;width:230px"></div>
  <div class="title" style="left:346px;top:240px;font-size:19px">Title <span>Goes Here</span></div>
  <div class="subtitle" style="left:346px;top:265px;font-size:7.5px">Subtitle goes here</div>
  <div class="rule" style="left:290px;bottom:0;width:290px;height:8px"></div>
</section>

</body>
</html>
```